VerintaCore PowerPoint Presentation Design

I am looking for a PowerPoint design for a new company based in Dallas, Texas called VerintaCore. We provide extremely powerful predictive and prescriptive analytics software focused on the Internet of Things (IoT) market. Our initial products are called VRC Foundry and VRC Pulse. We would like to see designs that support our logo design, which is attached.

I AM LOOKING FOR A THEME TO BE DEVELOPED FOR THE TITLE SLIDE AND INSIDE SLIDES OF A PRESENTATION. I AM NOT LOOKING FOR SOMEONE TO TAKE MY CONTENT AND CREATE A COMPLETE PRESENTATION.

Target Market(s)

Advanced Analytics, Internet of Things

Industry/Entity Type

It Company

Requirements
Must have
• Bolder colors, but they must work with the logo
Nice to have
• I prefer that the design incorporate the them of "connectivity" or "connectedness" to reflect the IoT market and "intelligence" or "smart" to reflect the analytics aspect of the business
Should not have
• I don't want people represented in the graphics scheme

```html
<!DOCTYPE html>
<html lang="en">
<head>
<meta charset="UTF-8">
<title>VerintaCore – Content Slide</title>
<link href="https://fonts.googleapis.com/css2?family=Titillium+Web:wght@300;400;600;700&display=swap" rel="stylesheet">
<style>
  :root {
    --brand-blue: #003a9b;
    --title-blue: #0b3d95;
    --rule-gray: #9aa0a8;
    --icon-gray: #7a7a7a;
    --body-gray: #555555;
    --footer-orange: #ffaa00;
    --footer-rule: #1a1a1a;
    --white: #ffffff;
  }
  * { margin: 0; padding: 0; box-sizing: border-box; }
  html, body { width: 1200px; height: 900px; overflow: hidden; background: var(--white); }
  body { font-family: "Titillium Web", sans-serif; position: relative; }

  .slide { position: relative; width: 1200px; height: 900px; }

  .header {
    position: absolute; left: 0; top: 0; width: 1200px; height: 90px;
    background: var(--brand-blue);
    display: flex; align-items: center; justify-content: space-between;
    padding: 0 18px 0 19px;
  }
  .header-rule {
    position: absolute; left: 0; top: 92px; width: 1200px; height: 3px;
    background: var(--rule-gray);
  }
  .project-title {
    color: var(--white); font-weight: 700; font-size: 44px; letter-spacing: 0.2px;
  }
  .brand-name {
    color: var(--white); font-weight: 600; font-size: 52px; letter-spacing: 0.5px;
  }

  .feature { position: absolute; left: 0; width: 1200px; }
  .feature-icon {
    position: absolute; width: 108px; height: 108px; border-radius: 50%;
    background: var(--icon-gray);
    display: flex; align-items: center; justify-content: center;
  }
  .feature-icon svg { width: 32px; height: 32px; }
  .feature-text { position: absolute; left: 235px; width: 930px; }
  .feature-title {
    color: var(--title-blue); font-weight: 400; font-size: 30px; line-height: 40px;
  }
  .feature-body {
    color: var(--body-gray); font-weight: 300; font-size: 19.5px; line-height: 33px;
    margin-top: 10px;
  }

  .footer-rule {
    position: absolute; left: 0; top: 846px; width: 1200px; height: 3px;
    background: var(--footer-rule);
  }
  .footer {
    position: absolute; left: 0; top: 849px; width: 1200px; height: 51px;
    background: var(--footer-orange);
    display: flex; align-items: center; justify-content: space-between;
    padding: 0 13px 0 12px; color: var(--white); font-weight: 600; font-size: 21px;
  }
</style>
</head>
<body>
<div class="slide">
  <header class="header">
    <h1 class="project-title">Project Title Here</h1>
    <div class="brand-name">VerintaCore</div>
  </header>
  <div class="header-rule"></div>

  <section class="feature" style="top:196px;">
    <div class="feature-icon" style="left:90px; top:0;">
      <svg viewBox="0 0 24 24" aria-hidden="true">
        <rect x="2" y="2" width="20" height="20" rx="3" fill="#fff"/>
        <path d="M6.5 12.5l3.5 3.5 7.5-8" fill="none" stroke="#7a7a7a" stroke-width="2.6" stroke-linecap="round" stroke-linejoin="round"/>
      </svg>
    </div>
    <div class="feature-text" style="top:-4px;">
      <h2 class="feature-title">Text Titlte Here</h2>
      <p class="feature-body">Lorem ipsum dolor sit Lorem ipsum dolor sit&nbsp; Lorem ipsum dolor sit Lorem ipsum dolor sit&nbsp; Lorem ipsum dolor sit Lorem ipsum dolor sit&nbsp; Lorem ipsum dolor sit Lorem ipsum dolor sit&nbsp; Lorem ipsum dolor sit Lorem ipsum dolor sit&nbsp; Lorem ipsum dolor sit Lorem ipsum dolor sit&nbsp; Lorem ipsum dolor sit Lorem ipsum dolor sit</p>
    </div>
  </section>

  <section class="feature" style="top:379px;">
    <div class="feature-icon" style="left:82px; top:0;">
      <svg viewBox="0 0 24 24" aria-hidden="true">
        <rect x="1.5" y="7" width="21" height="10" rx="5" fill="#fff"/>
        <path d="M5.5 12h4M7.5 10v4" stroke="#7a7a7a" stroke-width="1.6" stroke-linecap="round"/>
        <circle cx="16" cy="11" r="1.1" fill="#7a7a7a"/>
        <circle cx="18.2" cy="13" r="1.1" fill="#7a7a7a"/>
      </svg>
    </div>
    <div class="feature-text" style="top:-14px;">
      <h2 class="feature-title">Text Titlte Here</h2>
      <p class="feature-body">Lorem ipsum dolor sit Lorem ipsum dolor sit&nbsp; Lorem ipsum dolor sit Lorem ipsum dolor sit&nbsp; Lorem ipsum dolor sit Lorem ipsum dolor sit&nbsp; Lorem ipsum dolor sit Lorem ipsum dolor sit&nbsp; Lorem ipsum dolor sit Lorem ipsum dolor sit&nbsp; Lorem ipsum dolor sit Lorem ipsum dolor sit&nbsp; Lorem ipsum dolor sit Lorem ipsum dolor sit</p>
    </div>
  </section>

  <section class="feature" style="top:584px;">
    <div class="feature-icon" style="left:87px; top:0;">
      <svg viewBox="0 0 24 24" aria-hidden="true">
        <rect x="2" y="3.5" width="20" height="14" rx="1.5" fill="#fff"/>
        <rect x="9.5" y="17.5" width="5" height="2.5" fill="#fff"/>
        <rect x="7" y="19.5" width="10" height="1.8" rx="0.6" fill="#fff"/>
      </svg>
    </div>
    <div class="feature-text" style="top:0;">
      <h2 class="feature-title">Text Titlte Here</h2>
      <p class="feature-body">Lorem ipsum dolor sit Lorem ipsum dolor sit&nbsp; Lorem ipsum dolor sit Lorem ipsum dolor sit&nbsp; Lorem ipsum dolor sit Lorem ipsum dolor sit&nbsp; Lorem ipsum dolor sit Lorem ipsum dolor sit&nbsp; Lorem ipsum dolor sit Lorem ipsum dolor sit&nbsp; Lorem ipsum dolor sit Lorem ipsum dolor sit&nbsp; Lorem ipsum dolor sit Lorem ipsum dolor sit</p>
    </div>
  </section>

  <div class="footer-rule"></div>
  <footer class="footer">
    <span class="copyright">Copyright text here</span>
    <span class="page-number">Page :01</span>
  </footer>
</div>
</body>
</html>
```